VAN WRAP

I would like to have my logo for my electrical contracting company on my 2018 kestrel haulmar 310 lab short roof. I do like the white front and black back. The business is located st George Utah. web site is www.pylonvoltworks.us and phone number is 5550187246.

```html
<!DOCTYPE html>
<html lang="en">
<head>
<meta charset="utf-8">
<title>Pylon Voltworks – Van Wrap Side Panel</title>
<link rel="stylesheet" href="https://fonts.googleapis.com/css2?family=Montserrat:wght@500;800&family=Roboto:wght@500;700&display=swap">
<style>
  :root {
    --wrap-white: #ffffff;
    --wrap-black: #0b0b0b;
    --accent-red: #e3262f;
  }
  html, body {
    margin: 0;
    padding: 0;
    width: 1200px;
    height: 617px;
    overflow: hidden;
    background: var(--wrap-white);
  }
  .wrap-panel {
    display: block;
    width: 1200px;
    height: 617px;
  }
  .panel-white { fill: var(--wrap-white); }
  .panel-black { fill: var(--wrap-black); }
  .brand-name {
    font-family: "Montserrat", sans-serif;
    font-weight: 800;
    font-size: 64px;
    letter-spacing: 1px;
    fill: var(--wrap-black);
  }
  .brand-tagline {
    font-family: "Montserrat", sans-serif;
    font-weight: 500;
    font-size: 22px;
    letter-spacing: 8px;
    fill: var(--wrap-black);
  }
  .brand-mark { fill: var(--accent-red); }
  .phone-number {
    font-family: "Roboto", sans-serif;
    font-weight: 700;
    font-size: 36px;
    letter-spacing: 1px;
    fill: var(--wrap-white);
  }
  .web-address {
    font-family: "Roboto", sans-serif;
    font-weight: 500;
    font-size: 20px;
    fill: var(--accent-red);
  }
  .phone-icon { fill: var(--accent-red); }
</style>
</head>
<body>
<svg class="wrap-panel" viewBox="0 0 1200 617" xmlns="http://www.w3.org/2000/svg">
  <rect class="panel-white" x="0" y="0" width="1200" height="617"/>
  <polygon class="panel-black" points="300,617 1200,160 1200,617"/>

  <g class="brand-lockup" transform="translate(350 560) rotate(-26.9)">
    <text class="brand-name" x="0" y="-20">PYLON VOLTWORKS</text>
    <text class="brand-tagline" x="8" y="14">ELECTRICAL CONTRACTORS</text>
  </g>

  <rect class="brand-mark" x="1050" y="240" width="110" height="110"/>

  <g class="phone-line">
    <path class="phone-icon" d="M768 446c-3 0-6 3-6 6 0 12 10 22 22 22 3 0 6-3 6-6v-4l-7-3-3 3c-4-2-7-5-9-9l3-3-3-7z"/>
    <text class="phone-number" x="798" y="472">5550187246</text>
  </g>
  <text class="web-address" x="808" y="504">www.pylonvoltworks.us</text>
</svg>
</body>
</html>
```